Marbol Gardens Business Card Design

My company is about Natural products made from Bees Wax, of which I am farming/raising. Products like Honey when in season, body butter, hand cream, lotions, lip balm, soap and more! All Natural, with Beeswax as the base, as it has large healing properties for moisturizing and nourishing your skin.
I would prefer lots of yellows, browns, and blacks (but am open)! I think black ink on the artwork may show up the best. But your the professionals!
The artwork is very dear to me, as my son, Warren did this in the hospital when he was diagnosed with Leukemia, of which he did not survive, at eighteen.
Is it possible to put his initials on this? WJT in light colored ink.
NO BEES, NO US! Oops! I need my name on there. Paula Dimmick and number 555-014-2297. Thank you all so much.

Hospital

Marbol Gardens
All Natural Products
Paula Dimmick
555-014-2297
MarbolGardens@plimmet.com

```html
<!DOCTYPE html>
<html lang="en">
<head>
<meta charset="utf-8">
<title>Marbol Gardens — Business Card</title>
<link rel="stylesheet" href="https://fonts.googleapis.com/css2?family=Josefin+Sans:wght@300&family=Parisienne&display=swap">
<style>
  :root {
    --paper: #ffffff;
    --gold: #f5a51c;
    --ember: #e8652c;
    --violet: #6a5fb0;
    --leaf: #8cc06a;
    --art-pink: #e8407a;
    --art-orange: #f7761e;
    --art-yellow: #f9d21e;
    --art-green: #64b43c;
    --art-purple: #7a3a8c;
    --art-blue: #4b5fb4;
    --initials: #fff3a8;
  }
  html, body {
    margin: 0;
    padding: 0;
    overflow: hidden;
    background: var(--paper);
  }
  .card {
    position: relative;
    width: 1200px;
    height: 702px;
    background: var(--paper);
    overflow: hidden;
    font-family: "Josefin Sans", "Helvetica Neue", Arial, sans-serif;
  }
  .artwork {
    position: absolute;
    left: 0;
    top: 0;
    width: 1200px;
    height: 702px;
  }
  .artwork-initials {
    position: absolute;
    left: 322px;
    top: 622px;
    width: 70px;
    text-align: center;
    font-size: 15px;
    color: var(--initials);
    letter-spacing: 0.5px;
  }
  .brand-name {
    position: absolute;
    right: 62px;
    top: 284px;
    margin: 0;
    font-weight: 300;
    font-size: 100px;
    line-height: 1;
    color: var(--gold);
    letter-spacing: 0;
  }
  .brand-script {
    position: absolute;
    right: 70px;
    top: 350px;
    margin: 0;
    font-family: "Parisienne", "Brush Script MT", cursive;
    font-size: 80px;
    line-height: 1;
    color: var(--ember);
    font-weight: 400;
  }
  .tagline {
    position: absolute;
    right: 62px;
    top: 460px;
    margin: 0;
    font-weight: 300;
    font-size: 25px;
    line-height: 1;
    color: var(--violet);
    letter-spacing: 0;
  }
  .rule {
    position: absolute;
    left: 718px;
    right: 0;
    top: 503px;
    border-top: 1.5px dashed var(--leaf);
  }
  .contact {
    position: absolute;
    right: 70px;
    top: 530px;
    margin: 0;
    text-align: right;
    font-weight: 300;
    font-size: 23px;
    line-height: 38px;
    color: var(--ember);
    text-transform: uppercase;
    letter-spacing: 0.5px;
    font-style: normal;
  }
  .contact span { display: block; }
</style>
</head>
<body>
  <main class="card">
    <svg class="artwork" viewBox="0 0 1200 702" role="img" aria-label="Hand-painted patchwork bee artwork in pink, orange, yellow, green, purple and blue">
      <defs>
        <linearGradient id="art-base" x1="0" y1="1" x2="1" y2="0">
          <stop offset="0" stop-color="var(--art-pink)"/>
          <stop offset="0.5" stop-color="var(--art-orange)"/>
          <stop offset="1" stop-color="var(--art-yellow)"/>
        </linearGradient>
        <radialGradient id="art-wing" cx="0.62" cy="0.28" r="0.3">
          <stop offset="0" stop-color="var(--art-yellow)"/>
          <stop offset="0.55" stop-color="var(--art-green)" stop-opacity="0.5"/>
          <stop offset="1" stop-color="var(--art-yellow)" stop-opacity="0"/>
        </radialGradient>
        <radialGradient id="art-left" cx="0.08" cy="0.4" r="0.22">
          <stop offset="0" stop-color="var(--art-purple)"/>
          <stop offset="1" stop-color="var(--art-purple)" stop-opacity="0"/>
        </radialGradient>
        <radialGradient id="art-body" cx="0.3" cy="0.55" r="0.2">
          <stop offset="0" stop-color="var(--art-blue)"/>
          <stop offset="1" stop-color="var(--art-green)" stop-opacity="0"/>
        </radialGradient>
        <clipPath id="art-shape">
          <path d="M0,190 C70,175 150,195 205,225 C225,130 265,40 330,65 C385,88 425,140 445,215 C570,165 730,140 860,168 C885,180 875,230 800,245 C740,258 690,268 662,300 C632,360 640,440 662,520 C630,540 585,525 545,545 C565,625 505,700 385,702 L300,702 C255,700 240,645 232,605 C180,645 110,630 40,565 L0,540 Z"/>
        </clipPath>
      </defs>
      <g clip-path="url(#art-shape)">
        <rect width="1200" height="702" fill="url(#art-base)"/>
        <rect width="1200" height="702" fill="url(#art-wing)"/>
        <rect width="1200" height="702" fill="url(#art-left)"/>
        <rect width="1200" height="702" fill="url(#art-body)"/>
      </g>
    </svg>
    <div class="artwork-initials">W.J.T</div>

    <h1 class="brand-name">MARBOL</h1>
    <p class="brand-script">gardens</p>
    <p class="tagline">ALL NATURAL BEE WAX PRODUCTS</p>
    <div class="rule"></div>

    <address class="contact">
      <span class="contact-name">Paula Dimmick</span>
      <span class="contact-phone">555·014·2297</span>
      <span class="contact-email">MarbolGardens@plimmet.com</span>
    </address>
  </main>
</body>
</html>
```